Automotive component supplier needs a business card design

We need a business card design for our company called Velmar Global Components Ltd based in the UK. We are a supplier of interior and exterior components to premium car manufacturers such as Corvane Hale, Durrant Fyfe, Maxtorn and Valdessimo. We would like to see a modern business card design that uses the colour blue.

Target Market(s)

Premium automotive car manufacturers.

Industry/Entity Type

Automotive

Contact Information for Business Card

Company Name : Velmar Global Components Limited
Address: 17 Tamsey Yard, Upper Drisk, Warwick, CV31 8RJ, United Kingdom
Web Address : www.velmarparts-example.co.uk

Font styles to use
Other font styles liked:
• Helvetica

Colors
3176b5
0255a3
85acd3
cfdeed
cee9f5
85cae6
34a6d7
0692cd
9bcb3c

Requirements
Must have
• Clear company logo and a mixture of blue colours.
Nice to have
• A high quality modern image.
Should not have
• Multiple colours.

```html
<!DOCTYPE html>
<html lang="en">
<head>
<meta charset="utf-8">
<title>Velmar Global Components – Business Card</title>
<link rel="stylesheet" href="https://fonts.googleapis.com/css2?family=Open+Sans:wght@400;600;700;800&display=swap">
<style>
  :root {
    --backdrop: #1f1f1f;
    --card-white: #ffffff;
    --brand-blue: #0a8fcf;
    --brand-green: #9bcb3c;
    --text-grey: #4a4a4a;
  }
  * { margin: 0; padding: 0; box-sizing: border-box; }
  html, body {
    width: 1200px; height: 987px; overflow: hidden;
    background: var(--backdrop);
    font-family: "Open Sans", Helvetica, Arial, sans-serif;
  }
  .card {
    position: absolute;
    width: 615px; height: 352px;
  }
  .card-front { left: 293px; top: 130px; background: var(--card-white); }
  .card-back  { left: 292px; top: 505px; background: var(--brand-blue); }

  .brand { position: absolute; left: 35px; top: 34px; color: var(--brand-blue); font-weight: 800; }
  .brand-name { font-size: 50px; line-height: 1; letter-spacing: 1px; }
  .brand-tagline { font-size: 14px; letter-spacing: 0.6px; margin-top: 4px; }

  .person { position: absolute; right: 35px; top: 152px; text-align: right; }
  .person-name { color: var(--brand-blue); font-weight: 700; font-size: 21px; line-height: 1; }
  .person-role { color: var(--brand-green); font-size: 15px; margin-top: 6px; }

  .divider { position: absolute; left: 35px; right: 35px; top: 212px; height: 1px; background: var(--brand-blue); }

  .contacts { position: absolute; left: 35px; top: 224px; list-style: none; }
  .contacts li { display: flex; align-items: center; height: 23.5px; font-size: 16px; color: var(--text-grey); }
  .contacts svg { width: 16px; height: 16px; margin-right: 7px; fill: var(--brand-blue); }

  .address { position: absolute; right: 35px; top: 226px; text-align: right; font-size: 16px; line-height: 23px; color: var(--text-grey); font-style: normal; }

  .web-bar {
    position: absolute; left: 0; top: 308px; width: 572px; height: 26px;
    background: var(--brand-blue); color: #fff; font-size: 15px; line-height: 26px; padding-left: 35px;
  }
  .accent-square {
    position: absolute; left: 574px; top: 307px; width: 37px; height: 28px;
    background: var(--brand-green); border-radius: 5px;
  }

  .back-brand {
    position: absolute; left: 0; right: 0; top: 138px; text-align: center;
    color: #fff; font-weight: 800; font-size: 72px; line-height: 1; letter-spacing: 2px;
  }
  .back-web {
    position: absolute; left: 0; right: 0; top: 284px; text-align: center;
    color: #fff; font-size: 15px; letter-spacing: 6px;
  }
</style>
</head>
<body>
  <section class="card card-front">
    <div class="brand">
      <div class="brand-name">VELMAR</div>
      <div class="brand-tagline">GLOBAL COMPONENTS</div>
    </div>

    <div class="person">
      <div class="person-name">RHYS CALDER</div>
      <div class="person-role">CEO/Founder</div>
    </div>

    <div class="divider"></div>

    <ul class="contacts">
      <li>
        <svg viewBox="0 0 16 16" aria-hidden="true"><path d="M3.5 1.2l2.3 2.6c.3.4.3.9 0 1.2L4.6 6.3c.8 1.9 2.9 4 4.9 4.9l1.3-1.2c.3-.3.9-.3 1.2 0l2.6 2.3c.4.3.4.9 0 1.2l-1.4 1.3c-.7.6-1.7.7-2.5.3C6.4 13.5 2.6 9.7 1 5.6c-.4-.9-.2-1.9.5-2.5L2.3 1.2c.3-.4.9-.4 1.2 0z"/></svg>
        689 555 0142
      </li>
      <li>
        <svg viewBox="0 0 16 16" aria-hidden="true"><path d="M4.5 0h7c.8 0 1.5.7 1.5 1.5v13c0 .8-.7 1.5-1.5 1.5h-7C3.7 16 3 15.3 3 14.5v-13C3 .7 3.7 0 4.5 0zm.3 2v10.5h6.4V2H4.8zM8 13.3a.9.9 0 100 1.8.9.9 0 000-1.8z"/></svg>
        836 555 0187
      </li>
      <li>
        <svg viewBox="0 0 16 16" aria-hidden="true"><path d="M1 4h14v9H1V4zm1.3 1.2v.2L8 9.2l5.7-3.8v-.2H2.3zm0 1.6v5h11.4v-5L8 10.6 2.3 6.8z"/></svg>
        rhys@velmarparts-example.co.uk
      </li>
    </ul>

    <address class="address">
      17 Tamsey Yard, Upper Drisk<br>
      Warwick, CV31 8RJ<br>
      United Kingdom
    </address>

    <div class="web-bar">www.velmarparts-example.co.uk</div>
    <div class="accent-square"></div>
  </section>

  <section class="card card-back">
    <div class="back-brand">VELMAR</div>
    <div class="back-web">www.velmarparts-example.co.uk</div>
  </section>
</body>
</html>
```